Webdesign für Malerbetrieb
Zielgruppe
Malerbetrieb
Zielgruppe: private Haushalte, Wohnungsverwaltungen
Aufgabenstellung
Das Logo bitte integrieren.
Die Seite darf auf meine potentielle Kunden freundlich und einladend wirken. Die Grundfarben des Logos sollen bitte dezent vertreten werden, die Farbharmonie dabei sollte stimmen.
Da ich kein eigenes Bildmaterial habe, sind natürlich themabezogene Stock-Bilder erwünscht, aber wenn möglich bitte ohne Personen und die Seite nicht mit großen XXL-Bildern überladen.
Ansonsten lasse ich mich gerne von eurer Kreativität überraschen!

```html
<!DOCTYPE html>
<html lang="de">
<head>
<meta charset="utf-8">
<title>Lutz Malereibetrieb – Mobile Startseite</title>
<link rel="stylesheet" href="https://fonts.googleapis.com/css2?family=Roboto+Condensed:wght@300;400;700&family=Open+Sans:wght@300;400&display=swap">
<style>
  :root {
    --page-bg: #e6e6e4;
    --screen-bg: #050505;
    --cyan: #27a8e0;
    --yellow: #f4e61c;
    --magenta: #e0218a;
    --white: #ffffff;
    --muted: #bdbdbd;
  }
  * { box-sizing: border-box; margin: 0; padding: 0; }
  html, body {
    width: 1200px; height: 801px; overflow: hidden;
    background: var(--page-bg);
  }
  .mobile-page {
    position: absolute; left: 392px; top: 30px;
    width: 416px; height: 740px;
    background: var(--screen-bg);
    overflow: hidden;
    font-family: "Open Sans", sans-serif;
    color: var(--white);
  }
  .hero-photo {
    position: absolute; right: 0; top: 0;
    width: 300px; height: 600px;
    background:
      radial-gradient(ellipse at 70% 25%, rgba(70,90,110,.75) 0%, rgba(40,45,55,.6) 35%, rgba(5,5,5,0) 70%),
      radial-gradient(circle at 40% 15%, rgba(200,50,40,.45) 0%, rgba(0,0,0,0) 18%),
      radial-gradient(circle at 55% 45%, rgba(220,170,50,.35) 0%, rgba(0,0,0,0) 20%),
      radial-gradient(ellipse at 75% 85%, rgba(60,70,90,.6) 0%, rgba(5,5,5,0) 55%);
  }
  .site-header {
    position: absolute; left: 0; top: 0; width: 100%;
    display: flex; justify-content: space-between; align-items: flex-start;
    padding: 34px 26px 0 30px;
  }
  .brand { display: flex; flex-direction: column; gap: 3px; }
  .brand-row { display: flex; align-items: center; gap: 8px; }
  .brand-mark { width: 12px; height: 12px; background: var(--white); }
  .brand-name {
    font-family: "Roboto Condensed", sans-serif;
    font-weight: 700; font-size: 30px; letter-spacing: 1px; line-height: 1;
    color: var(--white);
  }
  .brand-tagline {
    font-family: "Roboto Condensed", sans-serif;
    font-weight: 300; font-size: 9px; color: var(--muted);
  }
  .menu-toggle { display: flex; flex-direction: column; gap: 4px; margin-top: 6px; }
  .menu-toggle span { display: block; width: 20px; height: 2px; background: var(--muted); }
  .hero-copy {
    position: absolute; left: 34px; top: 330px; width: 360px;
  }
  .hero-title {
    font-family: "Roboto Condensed", sans-serif;
    line-height: .98;
  }
  .hero-title .line { display: block; }
  .line-light { font-weight: 300; font-size: 54px; color: var(--cyan); }
  .line-yellow { font-weight: 700; font-size: 56px; color: var(--yellow); letter-spacing: -1px; }
  .line-magenta { font-weight: 700; font-size: 62px; color: var(--magenta); letter-spacing: -1px; }
  .hero-text {
    margin-top: 18px;
    font-weight: 300; font-size: 14px; line-height: 1.45;
    text-transform: uppercase; letter-spacing: .3px;
  }
  .scroll-hint {
    position: absolute; left: 50%; bottom: 40px; transform: translateX(-50%);
    display: flex; flex-direction: column; align-items: center; gap: 8px;
    font-size: 8px; letter-spacing: 1px; color: var(--muted);
  }
</style>
</head>
<body>
  <main class="mobile-page">
    <div class="hero-photo" role="img" aria-label="Stockfoto: Haut mit Farbpigmenten in Blau, Gelb und Rot auf dunklem Grund"></div>

    <header class="site-header">
      <div class="brand">
        <div class="brand-row">
          <span class="brand-mark"></span>
          <span class="brand-name">LUTZ MALEREIBETRIEB</span>
        </div>
        <span class="brand-tagline">Qualität ist unsere Lieblingsfarbe</span>
      </div>
      <div class="menu-toggle" aria-label="Menü"><span></span><span></span><span></span></div>
    </header>

    <section class="hero-copy">
      <h1 class="hero-title">
        <span class="line line-light">Qualität ist</span>
        <span class="line line-yellow">Unsere</span>
        <span class="line line-magenta">Lieblingsfarbe</span>
      </h1>
      <p class="hero-text">Pünktlichkeit, Freundlichkeit<br>und Gewissenhaftigkeit<br>in Hamburg und Umgebung.</p>
    </section>

    <div class="scroll-hint">
      <span>SCROLL DOWN</span>
      <svg width="18" height="28" viewBox="0 0 18 28" aria-hidden="true">
        <rect x="1" y="1" width="16" height="26" rx="8" fill="none" stroke="#ffffff" stroke-width="1.5"/>
        <line x1="9" y1="7" x2="9" y2="12" stroke="#ffffff" stroke-width="1.5" stroke-linecap="round"/>
      </svg>
    </div>
  </main>
</body>
</html>
```